Professional and creatice Life Coach - Business Card design

I just relaunched my website and now i a need a correspoonding business card for my task as life coach. My website is www.tbalrond.com as reference. The compass is kind of a symbol for my work, as I help people navigate through their challenging phases in life. The business card should be colorful, but not too playful as I also adress business people. So it sould be creative, but professional (also to suport my other business as Management Consultant)

Target Market(s)

People who want to get teir problems resolved, in business, partnership and other personal realms

Industry/Entity Type

Life Coaching

Contact Information for Business Card

Front side should include Name, Phone number, Email, Website and address

Font styles to use
Sans Serif

Colors
add136

Requirements
Must have
• "Mag. Leopold Brantner" -> Name
"Energetische Praxis" -> Jobtitle (describing my profession as life coach)
colours and style should match my website www.tbalrond.com
Nice to have
• a compass as a symbol

```html
<!DOCTYPE html>
<html lang="de">
<head>
<meta charset="utf-8">
<title>Leopold Brantner – Visitenkarte</title>
<link href="https://fonts.googleapis.com/css2?family=Roboto+Condensed:wght@400;700&family=Open+Sans:wght@400;600&display=swap" rel="stylesheet">
<style>
  :root {
    --green: #add136;
    --green-dark: #5aa33a;
    --charcoal: #4a4a4a;
    --charcoal-deep: #3b3b3b;
    --ink: #1e1e1e;
    --text-grey: #444;
    --band-grey: #d9d9d9;
    --paper: #ececec;
    --stage: #e6e6e6;
  }
  * { box-sizing: border-box; margin: 0; padding: 0; }
  html, body { width: 1200px; height: 801px; overflow: hidden; }
  body {
    background: var(--stage);
    font-family: "Open Sans", sans-serif;
    position: relative;
  }
  .card {
    position: absolute;
    top: 252px;
    width: 520px;
    height: 297px;
    overflow: hidden;
    box-shadow: 0 10px 30px rgba(0,0,0,.18);
  }
  .card--front { left: 55px; background: var(--paper); }
  .card--back {
    left: 625px;
    background: linear-gradient(160deg, #555 0%, var(--charcoal-deep) 100%);
  }

  /* front */
  .front__photo {
    position: absolute; left: 0; top: 0; width: 100%; height: 128px;
    background: linear-gradient(110deg, #5d5f5e 0%, #8a8c8c 40%, #a7a9a9 60%, #6b6d6c 100%);
  }
  .front__band {
    position: absolute; left: 0; top: 128px; width: 100%; height: 112px;
    background: var(--band-grey);
  }
  .front__name {
    position: absolute; left: 150px; top: 144px;
    font-family: "Roboto Condensed", sans-serif; font-weight: 700;
    font-size: 25px; text-transform: uppercase; letter-spacing: .2px;
    color: var(--green);
  }
  .front__name .title-prefix { color: var(--ink); }
  .front__job {
    position: absolute; left: 150px; top: 176px;
    font-size: 12px; letter-spacing: 2.6px; text-transform: uppercase;
    color: var(--text-grey);
  }
  .contact {
    position: absolute; display: flex; align-items: center; gap: 9px;
    font-size: 13px; color: var(--ink);
  }
  .contact__icon {
    width: 20px; height: 20px; border-radius: 4px; background: var(--green);
    display: flex; align-items: center; justify-content: center;
  }
  .contact--phone { left: 110px; top: 210px; }
  .contact--web { left: 270px; top: 210px; }
  .contact--mail { left: 270px; top: 240px; }

  /* back */
  .back__brand {
    position: absolute; left: 0; top: 40px; width: 100%;
    display: flex; justify-content: center; align-items: center; gap: 8px;
    font-family: "Roboto Condensed", sans-serif; font-weight: 700;
    font-size: 18px; letter-spacing: 2px; color: var(--green);
  }
  .back__brand-dot { width: 12px; height: 12px; border-radius: 50%; background: var(--green); }
  .back__heading {
    position: absolute; left: 0; top: 82px; width: 100%; text-align: center;
    font-family: "Roboto Condensed", sans-serif; font-weight: 700;
    font-size: 50px; letter-spacing: 1px; color: #fff;
  }
  .back__band {
    position: absolute; left: 0; top: 172px; width: 100%; height: 125px;
    background: linear-gradient(180deg, var(--green) 0%, #9cc02f 100%);
    color: #fff; text-align: center;
  }
  .back__pin {
    position: absolute; left: 50%; top: -13px; transform: translateX(-50%);
    width: 26px; height: 26px; border-radius: 50%; background: var(--green-dark);
    display: flex; align-items: center; justify-content: center;
  }
  .back__name {
    margin-top: 22px;
    font-family: "Roboto Condensed", sans-serif; font-weight: 700;
    font-size: 24px; text-transform: uppercase;
  }
  .back__job { font-size: 12px; text-transform: uppercase; margin-top: 2px; }
  .back__address {
    font-family: "Roboto Condensed", sans-serif; font-size: 14px; margin-top: 6px;
  }
</style>
</head>
<body>

<section class="card card--front">
  <div class="front__photo" role="img" aria-label="Schwarz-weiß Foto: Hand hält einen Kompass vor einer Landschaft"></div>
  <div class="front__band"></div>
  <h1 class="front__name"><span class="title-prefix">Mag.</span> Leopold Brantner</h1>
  <p class="front__job">Energetische Praxis</p>

  <p class="contact contact--phone">
    <span class="contact__icon">
      <svg width="12" height="14" viewBox="0 0 12 14"><rect x="2" y="1" width="8" height="12" rx="1.5" fill="none" stroke="#fff" stroke-width="1.5"/><circle cx="6" cy="10.5" r=".9" fill="#fff"/></svg>
    </span>+43 660 4817392
  </p>
  <p class="contact contact--web">
    <span class="contact__icon">
      <svg width="14" height="14" viewBox="0 0 14 14" fill="none" stroke="#fff" stroke-width="1.2"><circle cx="7" cy="7" r="5.5"/><ellipse cx="7" cy="7" rx="2.5" ry="5.5"/><path d="M1.5 7h11M2.5 4h9M2.5 10h9"/></svg>
    </span>www.tbalrond.com
  </p>
  <p class="contact contact--mail">
    <span class="contact__icon">
      <svg width="14" height="14" viewBox="0 0 14 14"><text x="7" y="11" text-anchor="middle" font-family="Open Sans, sans-serif" font-size="12" fill="#fff">@</text></svg>
    </span>leopold@brantner.one
  </p>
</section>

<section class="card card--back">
  <p class="back__brand"><span class="back__brand-dot"></span>BRANTNER</p>
  <h2 class="back__heading">KONTAKT</h2>
  <div class="back__band">
    <span class="back__pin">
      <svg width="12" height="14" viewBox="0 0 12 14"><path d="M6 13S1.5 8 1.5 5a4.5 4.5 0 0 1 9 0C10.5 8 6 13 6 13z" fill="#fff"/><circle cx="6" cy="5" r="1.7" fill="#5aa33a"/></svg>
    </span>
    <p class="back__name">Mag. Leopold Brantner</p>
    <p class="back__job">Energetische Praxis</p>
    <p class="back__address">Lindenweg 12, 5020 Grünau, Österreich</p>
  </div>
</section>

</body>
</html>
```